Tidewalk Intro Course QM Dive Bonaire

QM Dive is looking for a great flyer to promote our Tidewalk Intro Course around Bonaire, the Caribbean.

Bonaire is shore dive capital of the world.
Our guests rent a pick-up truck. we would like to inform them about the possibilities of the Tidewalk Intro Dive.

We have the logo, images and text available. Its the catchy and mind blowing design we are looking for to create an eye-catch flyer.
One side will be in English, the other side will be in Dutch.

Target Market(s)

Visitors (non divers) of the island Bonaire

Industry/Entity Type

Diving industry

Font styles to use
Sans Serif

Colors
0094D4
00A9DD
6FCCEA
C7EBF8
E9F6FB
F0912C
F2A743
F7CA91
FBE8D2
FDF5EE

Requirements
Must have
• The picture with the car and divers next to it is mandatory. Inspire to go for a tidewalk intro dive, show the beauty under water, easy to come dive with us, just takes half a day
Should not have
• Should not have pictures taken not around Bonaire.

```html
<!DOCTYPE html>
<html lang="en">
<head>
<meta charset="utf-8">
<title>Tidewalk Intro Course – QM Dive Bonaire</title>
<link href="https://fonts.googleapis.com/css2?family=Kanit:ital,wght@1,800&family=Open+Sans:wght@400;600;700;800&display=swap" rel="stylesheet">
<style>
  :root{
    --navy:#22305e;
    --orange:#F0912C;
    --blue:#0094D4;
    --blue-light:#6FCCEA;
    --stage:#e4e5e7;
    --white:#ffffff;
  }
  *{box-sizing:border-box;margin:0;padding:0}
  html,body{width:1200px;height:2900px;overflow:hidden}
  body{background:var(--stage);font-family:"Open Sans",sans-serif;position:relative}

  .flyer{position:absolute;left:88px;width:1024px;height:1400px;background:var(--navy);overflow:hidden;box-shadow:0 6px 18px rgba(0,0,0,.18)}
  .flyer--en{top:20px}
  .flyer--nl{top:1460px}

  .hero-photo{position:absolute;left:0;top:0;width:1024px;height:420px;
    background:linear-gradient(180deg,#7fc3ea 0%,#b9e0f2 38%,#3fa9c9 52%,#e9dcc4 70%,#d8c7a6 100%)}
  .hero-wave{position:absolute;left:0;top:320px;width:1024px;height:140px}

  .reef-photo{position:absolute;left:770px;top:226px;width:220px;height:220px;border-radius:50%;
    border:8px solid var(--white);
    background:radial-gradient(circle at 40% 35%,#4fb7c8 0%,#1f7f93 55%,#0f4f63 100%)}

  .brand{position:absolute;left:40px;top:318px;display:flex;align-items:center;gap:12px}
  .brand-dot{width:34px;height:34px;border-radius:50%;background:var(--orange)}
  .brand-name{font-weight:800;font-size:32px;color:var(--navy);letter-spacing:.5px}

  .headline{position:absolute;left:0;top:470px;width:1024px;text-align:center;
    font-family:"Kanit",sans-serif;font-style:italic;font-weight:800;color:var(--orange);
    text-transform:uppercase;letter-spacing:.5px;line-height:1.2}
  .flyer--en .headline{font-size:46px}
  .flyer--nl .headline{font-size:38px;top:476px}

  .intro{position:absolute;left:92px;top:544px;width:840px;text-align:center;color:var(--white);
    font-size:21px;line-height:1.45}

  .col{position:absolute;top:680px;color:var(--white)}
  .col--left{left:50px;width:450px}
  .col--right{left:540px;width:440px}

  .pill{display:inline-block;background:var(--orange);color:var(--white);font-weight:700;font-size:18px;
    text-transform:uppercase;padding:10px 26px;border-radius:30px;margin-bottom:22px;letter-spacing:.3px}

  .facts{list-style:none;font-size:20px;line-height:1.4}
  .facts li{position:relative;padding-left:22px;margin-bottom:13px}
  .facts li::before{content:"";position:absolute;left:2px;top:11px;width:8px;height:8px;border-radius:50%;background:var(--blue-light)}

  .copy{font-size:20px;line-height:1.45;margin-bottom:28px}
  .call{font-size:23px;line-height:1.4;font-weight:700}
  .call em{font-style:normal;color:var(--orange)}

  .footer-wave{position:absolute;left:0;top:1250px;width:1024px;height:150px}
  .badge{position:absolute;left:890px;top:1180px;width:96px;height:96px;border-radius:50%;
    background:var(--white);border:10px solid var(--blue)}

  .contacts{position:absolute;left:40px;top:1338px;display:flex;gap:50px;align-items:center;
    font-size:19px;font-weight:600;color:var(--navy)}
  .contact{display:flex;align-items:center;gap:10px}
  .contact svg{width:30px;height:30px}
</style>
</head>
<body>

<section class="flyer flyer--en">
  <div class="hero-photo" role="img" aria-label="Two divers in gear standing beside a white rental pick-up truck on a Bonaire shore"></div>
  <svg class="hero-wave" viewBox="0 0 1024 140" preserveAspectRatio="none" aria-hidden="true">
    <path d="M0,55 C300,130 650,5 1024,45 L1024,140 L0,140Z" fill="#6FCCEA"/>
    <path d="M0,82 C300,150 650,32 1024,72 L1024,140 L0,140Z" fill="#22305e"/>
  </svg>
  <div class="reef-photo" role="img" aria-label="Underwater view of a diver over a coral reef"></div>
  <div class="brand"><span class="brand-dot"></span><span class="brand-name">QM Dive</span></div>

  <h1 class="headline">Tidewalk Intro Course on Bonaire</h1>
  <p class="intro">Fall in love with diving in our underwater paradise. Under the guidance of a dive instructor you will learn the basic skills for peaceful diving in a fun and easy way.</p>

  <div class="col col--left">
    <span class="pill">Develop a passion for marine life</span>
    <ul class="facts">
      <li>Ages 10 and up can sign up for our tidewalk intro dive</li>
      <li>You'll dive straight into the water after a brief theoretic introduction</li>
      <li>The Tidewalk Intro Course will take 3-4 hours</li>
      <li>Before participating, you are required to fill out a medical questionnaire</li>
      <li>A group consists of a maximum of 4 people</li>
      <li>Experience the splendor of the ocean without much distraction by other divers</li>
      <li>And enjoy a lot of personal attention given by your instructor</li>
    </ul>
  </div>

  <div class="col col--right">
    <span class="pill">Underwater paradise</span>
    <p class="copy">Bonaire is the place to learn how to scuba dive. After a brief introduction we will directly dive into the sea, where the reef starts in shallow waters. We have the perfect dive sites for beginners. Here, the sea bed slopes gradually down and you'll be amazed by the most beautiful fish and corals.</p>
    <p class="call">Stop by at our Front office and we are happy to answer all your questions or to book your <em>'Tidewalk Intro Dive'</em></p>
  </div>

  <svg class="footer-wave" viewBox="0 0 1024 150" preserveAspectRatio="none" aria-hidden="true">
    <path d="M0,50 C350,0 700,70 1024,20 L1024,150 L0,150Z" fill="#6FCCEA"/>
    <path d="M0,68 C350,22 700,88 1024,40 L1024,150 L0,150Z" fill="#ffffff"/>
  </svg>
  <div class="badge" aria-hidden="true"></div>

  <div class="contacts">
    <span class="contact">
      <svg viewBox="0 0 30 30" aria-hidden="true"><circle cx="15" cy="15" r="15" fill="#F0912C"/><circle cx="15" cy="15" r="8" fill="none" stroke="#fff" stroke-width="2"/><path d="M7 15h16M15 7c-4 5-4 11 0 16M15 7c4 5 4 11 0 16" fill="none" stroke="#fff" stroke-width="1.6"/></svg>
      www.qmdiving-bonaire.com</span>
    <span class="contact">
      <svg viewBox="0 0 30 30" aria-hidden="true"><circle cx="15" cy="15" r="15" fill="#F0912C"/><path d="M10 8l3 0 1.5 4-2 1.5a9 9 0 0 0 4 4l1.5-2 4 1.5 0 3c-7 1-13-5-12-12z" fill="#fff"/></svg>
      +(599) 555 01 42</span>
    <span class="contact">
      <svg viewBox="0 0 30 30" aria-hidden="true"><circle cx="15" cy="15" r="15" fill="#F0912C"/><rect x="7.5" y="10" width="15" height="10" rx="1" fill="#fff"/><path d="M7.5 10.5l7.5 5.5 7.5-5.5" fill="none" stroke="#F0912C" stroke-width="1.5"/></svg>
      hello@qmdiving-bonaire.com</span>
  </div>
</section>

<section class="flyer flyer--nl" lang="nl">
  <div class="hero-photo" role="img" aria-label="Twee duikers in uitrusting naast een witte huur-pick-up op de kust van Bonaire"></div>
  <svg class="hero-wave" viewBox="0 0 1024 140" preserveAspectRatio="none" aria-hidden="true">
    <path d="M0,55 C300,130 650,5 1024,45 L1024,140 L0,140Z" fill="#6FCCEA"/>
    <path d="M0,82 C300,150 650,32 1024,72 L1024,140 L0,140Z" fill="#22305e"/>
  </svg>
  <div class="reef-photo" role="img" aria-label="Onderwaterbeeld van een duiker boven een koraalrif"></div>
  <div class="brand"><span class="brand-dot"></span><span class="brand-name">QM Dive</span></div>

  <h1 class="headline">Proefduik op Bonaire ( Tidewalk Intro Course )</h1>
  <p class="intro">Word verliefd op het gevoel van duiken in een onderwaterparadijs. Onder begeleiding van een duikinstructeur ontdek je op een makkelijke en leuke manier alle basisvaardigheden voor een heerlijke duik.</p>

  <div class="col col--left">
    <span class="pill">Liefde voor het waterleven</span>
    <ul class="facts">
      <li>Onze proefduik is voor iedereen vanaf 10 jaar</li>
      <li>Na een korte theoretische introductie geniet je meteen van een duik</li>
      <li>De activiteit duurt 3 tot 4 uur</li>
      <li>Je kunt meedoen wanneer je gezond genoeg bent om je uitrusting te dragen</li>
      <li>Een groep bestaat uit maximaal 4 personen</li>
      <li>Hierdoor ervaar je de pracht van de oceaan zonder afleiding van anderen</li>
      <li>En heeft de duikinstructeur veel tijd voor persoonlijke aandacht</li>
    </ul>
  </div>

  <div class="col col--right">
    <span class="pill">Onderwaterparadijs</span>
    <p class="copy">Bonaire is bij uitstek de plek voor een proefduik. Na een korte introductie stappen we direct de zee in waar het rif al vrij snel begint. Bovendien kennen we de perfecte duikspots voor beginners. Hier loopt de zeebodem in een langzaam tempo naar beneden en word je verrast door de mooiste vissen en koralen.</p>
    <p class="call">Kom gerust langs bij onze front-office. Wij zijn graag bereid je vragen te beantwoorden of om de <em>'Tidewalk Intro Dive'</em> te plannen.</p>
  </div>

  <svg class="footer-wave" viewBox="0 0 1024 150" preserveAspectRatio="none" aria-hidden="true">
    <path d="M0,50 C350,0 700,70 1024,20 L1024,150 L0,150Z" fill="#6FCCEA"/>
    <path d="M0,68 C350,22 700,88 1024,40 L1024,150 L0,150Z" fill="#ffffff"/>
  </svg>
  <div class="badge" aria-hidden="true"></div>

  <div class="contacts">
    <span class="contact">
      <svg viewBox="0 0 30 30" aria-hidden="true"><circle cx="15" cy="15" r="15" fill="#F0912C"/><circle cx="15" cy="15" r="8" fill="none" stroke="#fff" stroke-width="2"/><path d="M7 15h16M15 7c-4 5-4 11 0 16M15 7c4 5 4 11 0 16" fill="none" stroke="#fff" stroke-width="1.6"/></svg>
      www.qmdiving-bonaire.com</span>
    <span class="contact">
      <svg viewBox="0 0 30 30" aria-hidden="true"><circle cx="15" cy="15" r="15" fill="#F0912C"/><path d="M10 8l3 0 1.5 4-2 1.5a9 9 0 0 0 4 4l1.5-2 4 1.5 0 3c-7 1-13-5-12-12z" fill="#fff"/></svg>
      +(599) 555 01 42</span>
    <span class="contact">
      <svg viewBox="0 0 30 30" aria-hidden="true"><circle cx="15" cy="15" r="15" fill="#F0912C"/><rect x="7.5" y="10" width="15" height="10" rx="1" fill="#fff"/><path d="M7.5 10.5l7.5 5.5 7.5-5.5" fill="none" stroke="#F0912C" stroke-width="1.5"/></svg>
      hello@qmdiving-bonaire.com</span>
  </div>
</section>

</body>
</html>
```